Brightwell Circle OKAV: Global Policy to Local Action

We need two professional visuals that represent the vision and strategy of the organization. I attached two rough images of the first visual and one image of the second visual. I also attached a pdf of the narrative to give context for each visual.

Target Market(s)

Global Health Policy Makers

Colors
ec1f27

Requirements
Must have
• Two separate images representing the flow of the work

```html
<!DOCTYPE html>
<html lang="en">
<head>
<meta charset="utf-8">
<title>Brightwell Circle OKAV: Global Policy to Local Action</title>
<link rel="stylesheet" href="https://fonts.googleapis.com/css2?family=Oswald:wght@300;400;500;600&display=swap">
<style>
  :root {
    --red: #ec1f27;
    --segment-red: #d8232a;
    --purple: #55296f;
    --text-purple: #5a2d6e;
    --bar-grey: #4a4a4a;
    --label-grey: #555555;
    --white: #ffffff;
  }
  html, body {
    margin: 0;
    padding: 0;
    overflow: hidden;
    background: var(--white);
  }
  .canvas {
    position: relative;
    width: 1200px;
    height: 1086px;
    overflow: hidden;
    background: var(--white);
    font-family: "Oswald", "Arial Narrow", sans-serif;
    font-weight: 300;
  }
  .diagram {
    position: absolute;
    left: 0;
    top: 0;
  }
  .tagline {
    position: absolute;
    top: 268px;
    left: 0;
    width: 1200px;
    text-align: center;
    color: var(--red);
    font-size: 15px;
    margin: 0;
  }
  .panel {
    position: absolute;
    width: 214px;
  }
  .panel-title {
    margin: 0;
    text-align: center;
    color: var(--red);
    font-weight: 600;
    font-size: 17px;
    line-height: 20px;
  }
  .panel-bar {
    height: 13px;
    background: var(--bar-grey);
    margin-top: 6px;
  }
  .panel-list {
    list-style: none;
    margin: 9px 0 0;
    padding: 0;
    color: var(--text-purple);
    font-size: 15.5px;
    line-height: 16px;
  }
  .panel-list li {
    position: relative;
    padding-left: 21px;
    margin-bottom: 7px;
  }
  .check {
    position: absolute;
    left: 1px;
    top: 1px;
    width: 13px;
    height: 13px;
    background: var(--red);
  }
  .check svg { display: block; }
  .panel-text {
    margin: 9px 0 0;
    color: var(--text-purple);
    font-size: 15.5px;
    line-height: 22px;
  }
  .frameworks { left: 162px; top: 303px; }
  .values { left: 826px; top: 297px; }
  .values .panel-list li { margin-bottom: 6px; }
  .knowledge { left: 162px; top: 643px; }
  .outcome { left: 826px; top: 655px; }
  .outcome .panel-text { line-height: 17px; }
  .segment-label {
    font-family: "Oswald", "Arial Narrow", sans-serif;
    font-weight: 300;
    font-size: 16px;
    fill: var(--white);
  }
  .ring-label {
    font-family: "Oswald", "Arial Narrow", sans-serif;
    font-weight: 500;
    font-size: 16px;
    fill: var(--white);
    letter-spacing: 0.5px;
  }
  .track-label {
    font-family: "Oswald", "Arial Narrow", sans-serif;
    font-weight: 500;
    font-size: 15px;
    fill: var(--label-grey);
    letter-spacing: 0.5px;
  }
  .hub-name {
    font-family: "Oswald", "Arial Narrow", sans-serif;
    font-weight: 400;
    font-size: 9.5px;
    fill: #3a3a3a;
    letter-spacing: 0.4px;
  }
  .hub-caption {
    font-family: "Oswald", "Arial Narrow", sans-serif;
    font-weight: 300;
    font-size: 8.5px;
    fill: #333333;
  }
</style>
</head>
<body>
<div class="canvas">

  <svg class="diagram" width="1200" height="1086" viewBox="0 0 1200 1086" aria-label="Cycle from global policy to local action">
    <defs>
      <radialGradient id="hubShade" cx="45%" cy="40%" r="65%">
        <stop offset="0%" stop-color="#ffffff"/>
        <stop offset="70%" stop-color="#f1f1f1"/>
        <stop offset="100%" stop-color="#cfcfcf"/>
      </radialGradient>
      <filter id="hubShadow" x="-30%" y="-30%" width="160%" height="160%">
        <feDropShadow dx="0" dy="3" stdDeviation="4" flood-color="#000" flood-opacity="0.35"/>
      </filter>
      <path id="ringTop" d="M 366 547 A 234 234 0 0 1 834 547"/>
      <path id="ringBottom" d="M 354 547 A 246 246 0 0 0 846 547"/>
      <path id="trackTop" d="M 415 547 A 185 185 0 0 1 785 547"/>
      <path id="trackBottom" d="M 400 547 A 200 200 0 0 0 800 547"/>
    </defs>

    <!-- outer cycle ring -->
    <circle class="cycle-ring" cx="600" cy="547" r="240" fill="none" stroke="var(--purple)" stroke-width="24"/>
    <polygon class="cycle-arrow" points="344,548 398,548 371,592" fill="var(--purple)"/>
    <polygon class="cycle-arrow" points="805,538 859,538 832,493" fill="var(--purple)"/>

    <text class="ring-label"><textPath href="#ringTop" startOffset="50%" text-anchor="middle">GLOBAL POLICY</textPath></text>
    <text class="ring-label"><textPath href="#ringBottom" startOffset="50%" text-anchor="middle">LOCAL ACTION</textPath></text>

    <text class="track-label"><textPath href="#trackTop" startOffset="30%" text-anchor="middle">POLICY PAPERS</textPath></text>
    <text class="track-label"><textPath href="#trackTop" startOffset="75%" text-anchor="middle">PUBLICATIONS</textPath></text>
    <text class="track-label"><textPath href="#trackBottom" startOffset="50%" text-anchor="middle">TRAINING CURRICULA</textPath></text>

    <!-- activity pinwheel -->
    <g class="pinwheel" transform="translate(600 547)">
      <circle r="165" fill="var(--segment-red)"/>
      <g class="pinwheel-dividers" fill="none" stroke="var(--white)" stroke-width="6">
        <path d="M 0 -66 C 45 -95 68 -135 58 -172"/>
        <path transform="rotate(72)" d="M 0 -66 C 45 -95 68 -135 58 -172"/>
        <path transform="rotate(144)" d="M 0 -66 C 45 -95 68 -135 58 -172"/>
        <path transform="rotate(216)" d="M 0 -66 C 45 -95 68 -135 58 -172"/>
        <path transform="rotate(288)" d="M 0 -66 C 45 -95 68 -135 58 -172"/>
      </g>
    </g>

    <text class="segment-label" x="579" y="432" text-anchor="middle">Regional</text>
    <text class="segment-label" x="579" y="449" text-anchor="middle">Meetings</text>
    <text class="segment-label" x="707" y="503" text-anchor="middle">Taskforces</text>
    <text class="segment-label" x="682" y="638" text-anchor="middle">Conferences</text>
    <text class="segment-label" x="561" y="682" text-anchor="middle">Symposiums</text>
    <text class="segment-label" x="478" y="544" text-anchor="middle">Workshops</text>

    <!-- central hub -->
    <g class="hub">
      <circle cx="601" cy="549" r="70" fill="url(#hubShade)" filter="url(#hubShadow)"/>
      <circle cx="561" cy="545" r="7" fill="var(--red)"/>
      <text class="hub-name" x="573" y="548">Brightwell Circle OKAV</text>
      <text class="hub-caption" x="601" y="585" text-anchor="middle">NETWORK OF NETWORKS</text>
    </g>
  </svg>

  <p class="tagline">OKAV drives is work through Gobal and Regional Partnerships</p>

  <section class="panel frameworks">
    <h2 class="panel-title">FRAMEWORKS</h2>
    <div class="panel-bar"></div>
    <ul class="panel-list">
      <li><span class="check"><svg width="13" height="13" viewBox="0 0 13 13"><path d="M3 6.5 L5.5 9 L10 4" fill="none" stroke="#5a1a1a" stroke-width="1.6"/></svg></span>Social Accountability &amp; Accreditation</li>
      <li><span class="check"><svg width="13" height="13" viewBox="0 0 13 13"><path d="M3 6.5 L5.5 9 L10 4" fill="none" stroke="#5a1a1a" stroke-width="1.6"/></svg></span>Interprofessional Education &amp; Team-based Care</li>
      <li><span class="check"><svg width="13" height="13" viewBox="0 0 13 13"><path d="M3 6.5 L5.5 9 L10 4" fill="none" stroke="#5a1a1a" stroke-width="1.6"/></svg></span>Population Health</li>
    </ul>
  </section>

  <section class="panel values">
    <h2 class="panel-title">GUIDING VALUES</h2>
    <div class="panel-bar"></div>
    <ul class="panel-list">
      <li><span class="check"><svg width="13" height="13" viewBox="0 0 13 13"><path d="M3 6.5 L5.5 9 L10 4" fill="none" stroke="#5a1a1a" stroke-width="1.6"/></svg></span>Community relevance</li>
      <li><span class="check"><svg width="13" height="13" viewBox="0 0 13 13"><path d="M3 6.5 L5.5 9 L10 4" fill="none" stroke="#5a1a1a" stroke-width="1.6"/></svg></span>Informed consumer</li>
      <li><span class="check"><svg width="13" height="13" viewBox="0 0 13 13"><path d="M3 6.5 L5.5 9 L10 4" fill="none" stroke="#5a1a1a" stroke-width="1.6"/></svg></span>Patient/Consumer voice</li>
      <li><span class="check"><svg width="13" height="13" viewBox="0 0 13 13"><path d="M3 6.5 L5.5 9 L10 4" fill="none" stroke="#5a1a1a" stroke-width="1.6"/></svg></span>Intersectoral, multi-disciplinary</li>
    </ul>
  </section>

  <section class="panel knowledge">
    <h2 class="panel-title">NETWORK&nbsp; KNOWLEDGE<br>BEST PRACTICES</h2>
    <div class="panel-bar"></div>
    <p class="panel-text">Remote/Rural, Woman, Migrants, Refugees, Indigenous Health</p>
  </section>

  <section class="panel outcome">
    <h2 class="panel-title">OUTCOME</h2>
    <div class="panel-bar"></div>
    <p class="panel-text">Coordinated Action by Local Change Agents and Networks</p>
  </section>

</div>
</body>
</html>
```